High end wine label at Austrian Winery

We are a traditional winery in Austria in region Burgenland. We are looking for a relaunch of our current wine label for our [vantor] series. It's a high end wine series at an upper price range. At the moment we have just two kinds of the label, one white one for the white wines and one black one for the red wines. This is a series of wine, white, red, sweet, sparkling and a top wine categories. So we need the same label, but in 4 different ways to distinguish the wines plus the sparkling. Maybe in color, patterns, ... or something else. The label should be very simple, including our new logo. It's also possible to make one label but we can splitting two parts of the label. The size of the label does not matter, need not be the same as now. It's a bit higher than a normal bottle. Additionally we need a back label with wine description and the wine dates on it.

Target Market(s)

private consumers and restaurants, no retailers

Colors

Designer to choose colors to be used in the design.

Requirements
Must have
• simple label with 4 different categories (red, white, sweet, top) plus Frizzante label, new logo integrated, high end label. Just logo, grape variety and [vantor] as text on the front label as text
Nice to have
• It's just good, if there'sa possibility to have different colors of each grape variety (about 10 different), but all the same style. top Wines should have an extraordinary design, but familiar with the others
Should not have
• no cheap look

```html
<!DOCTYPE html>
<html lang="en">
<head>
<meta charset="utf-8">
<title>Weller – Welschriesling [Vantor] Label</title>
<link rel="stylesheet" href="https://fonts.googleapis.com/css2?family=Alex+Brush&family=Encode+Sans+Condensed:wght@400;600&family=Marcellus&display=swap">
<style>
  :root {
    --canvas: #ffffff;
    --brown-dark: #5a4800;
    --brown-light: #9e7c05;
    --gold-deep: #6a5200;
    --gold-bright: #e2c246;
    --ink: #5c4700;
    --paper: #ffffff;
    --paper-shade: #cfcdd2;
  }
  html, body {
    margin: 0;
    width: 1200px;
    height: 1200px;
    overflow: hidden;
    background: var(--canvas);
  }
  .canvas {
    position: relative;
    width: 1200px;
    height: 1200px;
  }
  .label {
    position: absolute;
    left: 383px;
    top: 40px;
    width: 434px;
    height: 1120px;
    background: linear-gradient(100deg, var(--paper) 30%, var(--paper-shade) 100%);
    overflow: hidden;
  }
  .band {
    position: absolute;
    background: linear-gradient(90deg, var(--gold-deep), var(--gold-bright) 50%, var(--gold-deep));
  }
  .band--top { left: 0; top: 0; width: 100%; height: 17px; }
  .band--bottom { left: 6px; top: 1102px; width: 428px; height: 16px; }
  .band--stripe { height: 13px; }
  .label__head {
    position: absolute;
    left: 0; top: 17px;
    width: 100%; height: 418px;
    background: linear-gradient(180deg, var(--brown-dark), var(--brown-light));
  }
  .label__seal {
    position: absolute;
    left: 0; top: 0;
  }
  .label__signature {
    position: absolute;
    left: 0; top: 150px;
    width: 100%;
    text-align: center;
    font-family: "Alex Brush", cursive;
    font-size: 50px;
    color: #ffffff;
    line-height: 1;
  }
  .label__house {
    position: absolute;
    left: 0; top: 618px;
    width: 100%;
    text-align: center;
    font-family: "Marcellus", serif;
    font-size: 56px;
    letter-spacing: 8px;
    color: var(--ink);
    line-height: 1;
  }
  .label__variety {
    position: absolute;
    left: 0; top: 982px;
    width: 100%;
    text-align: center;
    font-family: "Encode Sans Condensed", sans-serif;
    font-size: 38px;
    letter-spacing: 1px;
    color: var(--ink);
    line-height: 1;
  }
  .label__series {
    position: absolute;
    left: 0; top: 1045px;
    width: 100%;
    text-align: center;
    font-family: "Encode Sans Condensed", sans-serif;
    font-weight: 600;
    font-size: 28px;
    letter-spacing: 1px;
    color: var(--ink);
    line-height: 1;
  }
</style>
</head>
<body>
<main class="canvas">
  <section class="label" aria-label="Front wine label">
    <div class="band band--top"></div>
    <div class="label__head"></div>
    <div class="band band--stripe" style="left:0; top:447px; width:100px;"></div>
    <div class="band band--stripe" style="left:334px; top:447px; width:100px;"></div>
    <div class="band band--stripe" style="left:0; top:492px; width:100px;"></div>
    <div class="band band--stripe" style="left:334px; top:492px; width:100px;"></div>
    <svg class="label__seal" width="434" height="600" viewBox="0 0 434 600" aria-hidden="true">
      <circle cx="217" cy="470" r="111" fill="#ffffff"/>
      <circle cx="217" cy="470" r="88" fill="none" stroke="#6b5308" stroke-width="6"/>
    </svg>
    <div class="label__signature">Konrad Weller</div>
    <div class="label__house">WELLER</div>
    <div class="label__variety">WELSCHRIESLING</div>
    <div class="label__series">[VANTOR]</div>
    <div class="band band--bottom"></div>
  </section>
</main>
</body>
</html>
```